stars + comments Reviews website design (similar to grubly concept)

Please refer to attached logo and wire frames
----------------------------------------------------------------------------------------------------
we are a company based in egypt, seeking a design for a website that allows user to find doctors using search and filters.
also it allows user to review this doctor through providing comment and 1 to 5 stars
i need 4 main pages designs:
1- Doctors list/favorites list
2- Doctor view
3- Add doctor (3 steps)
4- Sign-in/sign up
5- Menu design
am into the colors teal/turquoise (though am open for different opinion)
i don't want the design theme to be doctors specific
am into the school of very clean, very neat, very simple
(chirpnet, pagecircle, snapmosaic designs are appealing to me)
Updates

Number of Pages Required

4 page

Font styles to use
Sans Serif

Colors
00a990
33b8a4

Requirements
Must have
• website will be bilingual/ bi-directional (English and Arabic)
• designer needs to provide another copy of the design with "right to left" orientation
• interactive button animation

```html
<!DOCTYPE html>
<html lang="en">
<head>
<meta charset="utf-8">
<title>Medrevo – Doctors</title>
<link href="https://fonts.googleapis.com/css2?family=Open+Sans:wght@400;600;700&display=swap" rel="stylesheet">
<style>
  :root{
    --teal:#00a990;
    --teal-light:#33b8a4;
    --ink:#333333;
    --muted:#666666;
    --line:#d6d6d6;
    --field:#ffffff;
    --bar:#ececec;
    --avatar:#dedede;
    --star:#f5b400;
    --heart-on:#e60000;
    --heart-off:#ffffff;
    --footer:#e2e2e2;
  }
  *{box-sizing:border-box;margin:0;padding:0}
  html,body{width:1200px;height:916px;overflow:hidden}
  body{font-family:"Open Sans",Arial,sans-serif;color:var(--ink);position:relative;
    background:linear-gradient(#d9d9d9 145px,#f4f4f4 420px,#ffffff 600px);}

  /* header */
  .site-header{position:absolute;left:0;top:0;width:1200px;height:88px;
    background:linear-gradient(#ffffff,#e9e9e9);border-bottom:1px solid #d4d4d4}
  .brand{position:absolute;left:60px;top:1px;width:257px;height:86px;background:var(--teal);
    display:flex;align-items:center;justify-content:center;gap:10px;color:#fff;
    font-weight:700;font-size:40px;letter-spacing:-0.5px}
  .brand-dot{width:34px;height:34px;border-radius:50%;background:#fff}
  .main-nav{position:absolute;top:6px;left:0;width:0}
  .nav-btn{position:absolute;top:0;width:74px;height:74px;border-radius:50%;
    background:#f3f3f3;box-shadow:0 1px 3px rgba(0,0,0,.25);display:flex;align-items:center;justify-content:center}
  .nav-btn span{width:62px;height:62px;border-radius:50%;background:var(--teal);
    display:flex;align-items:center;justify-content:center}
  .nav-home{left:474px}.nav-fav{left:612px}.nav-add{left:750px}
  .user-menu{position:absolute;left:984px;top:28px;width:156px;height:30px;border-radius:15px;
    background:var(--teal-light);color:#fff;font-size:13px;font-weight:600;display:flex;align-items:center;padding-left:50px}
  .user-menu .user-icon{position:absolute;left:-2px;top:-6px;width:42px;height:42px;border-radius:50%;
    background:var(--teal);border:2px solid #fff;display:flex;align-items:center;justify-content:center}
  .user-menu .caret{margin-left:14px}

  /* filters */
  .filter-bar{position:absolute;left:0;top:89px;width:1200px;height:56px;background:var(--bar);
    border-bottom:1px solid #d0d0d0}
  .field{position:absolute;top:11px;height:32px;background:var(--field);border:1px solid var(--line);
    font-size:13.5px;color:#555;display:flex;align-items:center;padding-left:11px}
  .field .btn{position:absolute;right:0;top:0;width:33px;height:30px;background:#e4e4e4;
    border-left:1px solid var(--line);display:flex;align-items:center;justify-content:center}
  .f-search{left:60px;width:211px;padding-left:19px}
  .f-spec{left:281px;width:211px}
  .f-sub{left:503px;width:211px}
  .f-area{left:724px;width:194px}
  .f-gender{left:926px;width:102px}
  .f-rating{left:1037px;width:102px}

  /* results */
  .results-tab{position:absolute;left:192px;top:190px;width:198px;height:52px;background:#fff;
    border-radius:28px 28px 0 0;font-size:15px;font-weight:600;padding:17px 0 0 38px;
    box-shadow:0 -1px 2px rgba(0,0,0,.08)}
  .doctor-list{position:absolute;left:166px;top:240px;width:870px;height:584px;border:1px solid #cfcfcf;background:#fff}
  .doctor{position:relative;height:97px;border-bottom:1px solid #d9d9d9;
    background:linear-gradient(#f7f7f7,#e9e9e9)}
  .doctor:last-child{border-bottom:none}
  .avatar{position:absolute;left:9px;top:9px;width:78px;height:78px;background:var(--avatar);border:1px solid #cfcfcf}
  .doctor-info{position:absolute;left:106px;top:10px;font-size:13.5px;line-height:21px;color:var(--muted)}
  .doctor-info .name{color:var(--ink)}
  .rating{position:absolute;left:703px;top:11px;display:flex;align-items:center;gap:2px;font-size:13px;color:var(--muted)}
  .rating .count{margin-left:6px}
  .fav{position:absolute;left:823px;top:60px}
  .fav.on path{fill:var(--heart-on);stroke:var(--heart-on)}

  /* footer */
  .site-footer{position:absolute;left:0;top:870px;width:1200px;height:46px;background:var(--footer);
    display:flex;align-items:center;justify-content:space-between;padding:0 60px;font-size:13px;color:#555}
  .social{display:flex;gap:14px;font-size:12px;color:#8a8a8a}
  .social span{display:flex;align-items:center;gap:5px}
  .social i{width:12px;height:12px;border:1.5px solid #a9a9a9;border-radius:50%;display:block}
</style>
</head>
<body>
<svg width="0" height="0" style="position:absolute">
  <defs>
    <linearGradient id="half"><stop offset="50%" stop-color="#f5b400"/><stop offset="50%" stop-color="#ffffff"/></linearGradient>
    <symbol id="star" viewBox="0 0 24 24"><path d="M12 1.8l3 6.6 7.2.8-5.4 4.9 1.5 7.1L12 17.6l-6.3 3.6 1.5-7.1L1.8 9.2 9 8.4z" stroke="#c99400" stroke-width="1"/></symbol>
    <symbol id="heart" viewBox="0 0 28 26"><path d="M14 24S2 16.5 2 8.5A6 6 0 0 1 14 6a6 6 0 0 1 12 2.5C26 16.5 14 24 14 24z" stroke="#bdbdbd" stroke-width="1.5" fill="#ffffff"/></symbol>
  </defs>
</svg>

<header class="site-header">
  <div class="brand"><span class="brand-dot"></span>Medrevo</div>
  <nav class="main-nav">
    <a class="nav-btn nav-home"><span><svg width="28" height="26" viewBox="0 0 28 26"><path d="M14 2L2 13h4v11h6v-7h4v7h6V13h4z" fill="#fff"/></svg></span></a>
    <a class="nav-btn nav-fav"><span><svg width="32" height="29" viewBox="0 0 28 26"><path d="M14 24S2 16.5 2 8.5A6 6 0 0 1 14 6a6 6 0 0 1 12 2.5C26 16.5 14 24 14 24z" fill="#fff"/></svg></span></a>
    <a class="nav-btn nav-add"><span><svg width="30" height="30" viewBox="0 0 30 30"><rect x="4" y="5" width="18" height="22" rx="2" fill="#fff"/><circle cx="22" cy="22" r="7" fill="#fff" stroke="#00a990" stroke-width="2"/><path d="M22 18v8M18 22h8" stroke="#00a990" stroke-width="2.2"/></svg></span></a>
  </nav>
  <div class="user-menu">
    <span class="user-icon"><svg width="20" height="20" viewBox="0 0 20 20" fill="none" stroke="#fff" stroke-width="1.6"><circle cx="10" cy="6.5" r="4"/><path d="M2.5 19c0-4 3.4-6.5 7.5-6.5s7.5 2.5 7.5 6.5z"/></svg></span>
    Omar Ziad
    <svg class="caret" width="11" height="7" viewBox="0 0 11 7"><path d="M0 0h11L5.5 7z" fill="#fff"/></svg>
  </div>
</header>

<section class="filter-bar">
  <div class="field f-search">Search<span class="btn"><svg width="15" height="15" viewBox="0 0 15 15" fill="none" stroke="#555" stroke-width="1.8"><circle cx="6" cy="6" r="4.6"/><path d="M9.5 9.5l4.5 4.5"/></svg></span></div>
  <div class="field f-spec">Specialization<span class="btn"><svg width="16" height="10" viewBox="0 0 16 10"><path d="M2 2l6 6 6-6" stroke="#444" stroke-width="3" fill="none"/></svg></span></div>
  <div class="field f-sub">Sub-specialization<span class="btn"><svg width="16" height="10" viewBox="0 0 16 10"><path d="M2 2l6 6 6-6" stroke="#444" stroke-width="3" fill="none"/></svg></span></div>
  <div class="field f-area">Area<span class="btn"><svg width="16" height="10" viewBox="0 0 16 10"><path d="M2 2l6 6 6-6" stroke="#444" stroke-width="3" fill="none"/></svg></span></div>
  <div class="field f-gender">Gender<span class="btn"><svg width="16" height="10" viewBox="0 0 16 10"><path d="M2 2l6 6 6-6" stroke="#444" stroke-width="3" fill="none"/></svg></span></div>
  <div class="field f-rating">Rating<span class="btn"><svg width="16" height="10" viewBox="0 0 16 10"><path d="M2 2l6 6 6-6" stroke="#444" stroke-width="3" fill="none"/></svg></span></div>
</section>

<main>
  <div class="results-tab">15,123 Doctors</div>
  <ul class="doctor-list">
    <li class="doctor">
      <div class="avatar" role="img" aria-label="Doctor profile photo"></div>
      <div class="doctor-info"><div class="name">Karim Hadid (1 Km away)</div><div>Anesthesiologist</div><div>73 Cedar Street, Mohandeseen</div></div>
      <div class="rating"><svg width="21" height="21" fill="#f5b400"><use href="#star"/></svg><svg width="21" height="21" fill="#f5b400"><use href="#star"/></svg><svg width="21" height="21" fill="#f5b400"><use href="#star"/></svg><svg width="21" height="21" fill="#f5b400"><use href="#star"/></svg><svg width="21" height="21" fill="url(#half)"><use href="#star"/></svg><span class="count">(123)</span></div>
      <svg class="fav" width="28" height="26"><use href="#heart"/></svg>
    </li>
    <li class="doctor">
      <div class="avatar" role="img" aria-label="Doctor profile photo"></div>
      <div class="doctor-info"><div class="name">Salma Fathy (9 kms away)</div><div>Dentidt</div><div>48 Olive Street, Nasr City</div></div>
      <div class="rating"><svg width="21" height="21" fill="#f5b400"><use href="#star"/></svg><svg width="21" height="21" fill="#f5b400"><use href="#star"/></svg><svg width="21" height="21" fill="#f5b400"><use href="#star"/></svg><svg width="21" height="21" fill="#f5b400"><use href="#star"/></svg><svg width="21" height="21" fill="url(#half)"><use href="#star"/></svg><span class="count">(123)</span></div>
      <svg class="fav on" width="28" height="26" viewBox="0 0 28 26"><path d="M14 24S2 16.5 2 8.5A6 6 0 0 1 14 6a6 6 0 0 1 12 2.5C26 16.5 14 24 14 24z" stroke-width="1.5"/></svg>
    </li>
    <li class="doctor">
      <div class="avatar" role="img" aria-label="Doctor profile photo"></div>
      <div class="doctor-info"><div class="name">Laila Hadid (8 Kms away)</div><div>Pediatrician</div><div>122 Palm Street, Mohandeseen</div></div>
      <div class="rating"><svg width="21" height="21" fill="#f5b400"><use href="#star"/></svg><svg width="21" height="21" fill="#f5b400"><use href="#star"/></svg><svg width="21" height="21" fill="#f5b400"><use href="#star"/></svg><svg width="21" height="21" fill="#f5b400"><use href="#star"/></svg><svg width="21" height="21" fill="url(#half)"><use href="#star"/></svg><span class="count">(123)</span></div>
      <svg class="fav" width="28" height="26"><use href="#heart"/></svg>
    </li>
    <li class="doctor">
      <div class="avatar" role="img" aria-label="Doctor profile photo"></div>
      <div class="doctor-info"><div class="name">Laila Hadid (8 Kms away)</div><div>Pediatrician</div><div>48 Palm Street, Mohandeseen</div></div>
      <div class="rating"><svg width="21" height="21" fill="#f5b400"><use href="#star"/></svg><svg width="21" height="21" fill="#f5b400"><use href="#star"/></svg><svg width="21" height="21" fill="#f5b400"><use href="#star"/></svg><svg width="21" height="21" fill="#f5b400"><use href="#star"/></svg><svg width="21" height="21" fill="url(#half)"><use href="#star"/></svg><span class="count">(123)</span></div>
      <svg class="fav" width="28" height="26"><use href="#heart"/></svg>
    </li>
    <li class="doctor">
      <div class="avatar" role="img" aria-label="Doctor profile photo"></div>
      <div class="doctor-info"><div class="name">Karim Hadid (1 Km away)</div><div>Anesthesiologist</div><div>73 Cedar Street, Mohandeseen</div></div>
      <div class="rating"><svg width="21" height="21" fill="#f5b400"><use href="#star"/></svg><svg width="21" height="21" fill="#f5b400"><use href="#star"/></svg><svg width="21" height="21" fill="#f5b400"><use href="#star"/></svg><svg width="21" height="21" fill="#f5b400"><use href="#star"/></svg><svg width="21" height="21" fill="url(#half)"><use href="#star"/></svg><span class="count">(123)</span></div>
      <svg class="fav" width="28" height="26"><use href="#heart"/></svg>
    </li>
    <li class="doctor">
      <div class="avatar" role="img" aria-label="Doctor profile photo"></div>
      <div class="doctor-info"><div class="name">Laila Hadid (8 Kms away)</div><div>Pediatrician</div><div>122 Palm Street, Mohandeseen</div></div>
      <div class="rating"><svg width="21" height="21" fill="#f5b400"><use href="#star"/></svg><svg width="21" height="21" fill="#f5b400"><use href="#star"/></svg><svg width="21" height="21" fill="#f5b400"><use href="#star"/></svg><svg width="21" height="21" fill="#f5b400"><use href="#star"/></svg><svg width="21" height="21" fill="url(#half)"><use href="#star"/></svg><span class="count">(123)</span></div>
      <svg class="fav" width="28" height="26"><use href="#heart"/></svg>
    </li>
  </ul>
</main>

<footer class="site-footer">
  <div class="social"><span><i></i>pagecircle</span><span><i></i>chirpnet</span><span><i></i>snapmosaic</span></div>
  <div class="copyright">Copyright © 2015 Medrevo. All Rights Reserved</div>
</footer>
</body>
</html>
```